Business Card Design Project

Need a business card with logo that is attached.
Company name: Tolmen Brisk Solutions, LLC
My name: Lorna Tolmen
Title: President
Phone number: 703-555-0148
Email: ltolmen@tolmenbrisksolutions.example
web site: www.tolmenbrisksolutions.example

Industry/Entity Type

Business

```html
<!DOCTYPE html>
<html lang="en">
<head>
<meta charset="utf-8">
<title>Tolmen Brisk Solutions, LLC — Business Card</title>
<link rel="stylesheet" href="https://fonts.googleapis.com/css2?family=Cinzel:wght@400&family=Exo+2:wght@300;400;500&display=swap">
<style>
  :root {
    --backdrop: #cfc9c0;
    --card-light: #ebe8e1;
    --card-dark: #3b3b3c;
    --bar-dark: #2a2a2b;
    --ink-dark: #2b2b2b;
    --brand-blue: #1f6fb2;
    --accent-blue: #2a9ad8;
    --logo-light: #e9e9e9;
    --white: #ffffff;
  }
  * { box-sizing: border-box; margin: 0; padding: 0; }
  html, body { width: 1200px; height: 787px; overflow: hidden; }
  body {
    background: var(--backdrop);
    position: relative;
    font-family: "Exo 2", "Trebuchet MS", sans-serif;
  }
  .card {
    position: absolute;
    top: 243px;
    width: 525px;
    height: 300px;
    border-radius: 4px;
    overflow: hidden;
    box-shadow: 0 6px 18px rgba(0,0,0,0.25);
  }
  .card--front { left: 50px; background: var(--card-light); }
  .card--back { left: 625px; background: var(--card-dark); }

  .brand {
    position: absolute;
    display: flex;
    align-items: center;
    gap: 12px;
  }
  .brand__mark {
    width: 40px; height: 40px;
    border-radius: 50%;
    flex: none;
  }
  .brand__name {
    font-family: "Cinzel", "Times New Roman", serif;
    font-weight: 400;
    line-height: 1.15;
    text-transform: uppercase;
    white-space: nowrap;
  }
  .card--front .brand { left: 30px; top: 118px; }
  .card--front .brand__mark { background: var(--brand-blue); }
  .card--front .brand__name { color: var(--brand-blue); font-size: 12px; }

  .name-bar {
    position: absolute;
    right: 0; top: 66px;
    width: 250px; height: 50px;
    background: var(--bar-dark);
    border-radius: 8px 0 0 8px;
    padding: 7px 48px 0 0;
    text-align: right;
  }
  .name-bar__name { color: var(--white); font-size: 17px; font-weight: 400; letter-spacing: 0.3px; line-height: 22px; }
  .name-bar__title { color: var(--accent-blue); font-size: 9px; letter-spacing: 1px; text-transform: uppercase; line-height: 12px; }
  .name-bar__slash { position: absolute; right: 16px; top: 12px; }

  .contact {
    position: absolute;
    right: 26px; bottom: 36px;
    list-style: none;
    text-align: right;
  }
  .contact__item {
    display: flex;
    justify-content: flex-end;
    align-items: center;
    gap: 8px;
    font-size: 12px;
    color: var(--ink-dark);
    line-height: 20px;
    white-space: nowrap;
  }
  .contact__icon { width: 14px; height: 14px; flex: none; }

  .card--back .brand { left: 50%; top: 50%; transform: translate(-50%, -50%); gap: 16px; }
  .card--back .brand__mark { width: 58px; height: 58px; background: var(--logo-light); }
  .card--back .brand__name { color: var(--logo-light); font-size: 17px; }
</style>
</head>
<body>
  <section class="card card--front" aria-label="Card front">
    <div class="brand">
      <span class="brand__mark"></span>
      <p class="brand__name">Tolmen Brisk<br>Solutions<br>LLC</p>
    </div>

    <div class="name-bar">
      <p class="name-bar__name">Lorna Tolmen</p>
      <p class="name-bar__title">President</p>
      <svg class="name-bar__slash" width="14" height="26" viewBox="0 0 14 26" aria-hidden="true">
        <polygon points="9,0 14,0 6,26 0,26" fill="var(--white)"/>
      </svg>
    </div>

    <ul class="contact">
      <li class="contact__item">703-555-0148
        <svg class="contact__icon" viewBox="0 0 14 14" aria-hidden="true">
          <rect x="1" y="1" width="12" height="12" fill="none" stroke="var(--accent-blue)" stroke-width="1.2"/>
          <path d="M4.5 3.5 L6 3.5 L6.5 5.5 L5.5 6.3 Q6.5 8 7.7 8.5 L8.5 7.5 L10.5 8 L10.5 9.5 Q6 10.5 4.5 3.5 Z" fill="var(--accent-blue)"/>
        </svg>
      </li>
      <li class="contact__item">ltolmen@tolmenbrisksolutions.example
        <svg class="contact__icon" viewBox="0 0 14 14" aria-hidden="true">
          <rect x="1" y="1" width="12" height="12" fill="none" stroke="var(--accent-blue)" stroke-width="1.2"/>
          <path d="M3 4 L11 4 L11 10 L3 10 Z M3 4 L7 7.5 L11 4" fill="none" stroke="var(--accent-blue)" stroke-width="1"/>
        </svg>
      </li>
      <li class="contact__item">www.tolmenbrisksolutions.example
        <svg class="contact__icon" viewBox="0 0 14 14" aria-hidden="true">
          <rect x="1" y="1" width="12" height="12" fill="none" stroke="var(--accent-blue)" stroke-width="1.2"/>
          <circle cx="7" cy="7" r="3.5" fill="none" stroke="var(--accent-blue)" stroke-width="1"/>
          <path d="M3.5 7 H10.5 M7 3.5 V10.5" stroke="var(--accent-blue)" stroke-width="0.8"/>
        </svg>
      </li>
    </ul>
  </section>

  <section class="card card--back" aria-label="Card back">
    <div class="brand">
      <span class="brand__mark"></span>
      <p class="brand__name">Tolmen Brisk<br>Solutions<br>LLC</p>
    </div>
  </section>
</body>
</html>
```